Facebook - Cover and profile picture

Hey, we need a cover pic and a picure for our sportsmanagement agency. I have uploaded a couple of files: Our Logo, our main Color, our old Picture Picture, which should be integrated into the cover Picture. We look forward to seeing your creative designs. If you have any questions, just ask.

```html
<!DOCTYPE html>
<html lang="de">
<head>
<meta charset="utf-8">
<title>KVR – Cover und Profilbild</title>
<link href="https://fonts.googleapis.com/css2?family=Montserrat:wght@600;700&family=Roboto:wght@400;500;700&display=swap" rel="stylesheet">
<style>
  :root {
    --stage: #161616;
    --brand-blue: #0a93c8;
    --bar-blue: #4267b2;
    --bar-dark: #29487d;
    --page-bg: #e9ebee;
    --paper: #f6f6f6;
    --photo-light: #f1f1f1;
    --photo-mid: #d6d6d6;
    --line-dark: #3b4450;
    --ui-text: #4b4f56;
    --ui-border: #ccd0d5;
    --badge: #fa3e3e;
    --white: #ffffff;
  }
  html, body {
    margin: 0;
    width: 1200px;
    height: 753px;
    overflow: hidden;
    background: var(--stage);
    font-family: "Roboto", Arial, sans-serif;
  }
  .canvas { position: relative; width: 1200px; height: 753px; }

  .page {
    position: absolute;
    left: 178px; top: 217px;
    width: 842px; height: 319px;
    background: var(--white);
    overflow: hidden;
  }
  .top-bar {
    position: absolute; left: 0; top: 0;
    width: 842px; height: 33px;
    background: var(--bar-blue);
    border-bottom: 1px solid var(--bar-dark);
    box-sizing: border-box;
  }
  .site-mark {
    position: absolute; left: 52px; top: 8px;
    width: 19px; height: 19px;
    background: var(--white); border-radius: 2px;
  }
  .search-box {
    position: absolute; left: 76px; top: 9px;
    width: 348px; height: 17px;
    background: var(--white); border-radius: 2px;
  }
  .search-button {
    position: absolute; right: 0; top: 0;
    width: 34px; height: 17px;
    background: #f6f7f9; border-left: 1px solid var(--ui-border);
  }
  .nav-link {
    position: absolute; top: 10px;
    color: var(--white); font-size: 10px; font-weight: 700;
  }
  .nav-link.home { left: 583px; }
  .nav-link.friends { left: 628px; }
  .nav-sep {
    position: absolute; left: 620px; top: 10px;
    width: 1px; height: 14px; background: var(--bar-dark);
  }
  .nav-icons { position: absolute; left: 697px; top: 6px; }

  .side-column {
    position: absolute; left: 0; top: 33px;
    width: 201px; height: 286px;
    background: var(--page-bg);
  }
  .side-menu { position: absolute; left: 48px; top: 211px; width: 144px; }
  .menu-item {
    height: 22px; line-height: 22px;
    padding-left: 7px; margin-bottom: 3px;
    font-size: 11.5px; color: var(--ui-text);
  }
  .menu-item.active { background: #f5f6f7; color: #1d2129; font-weight: 700; border-radius: 2px; }

  .profile-picture {
    position: absolute; left: 52px; top: 43px;
    width: 141px; height: 141px;
  }
  .cover-picture {
    position: absolute; left: 201px; top: 33px;
    width: 640px; height: 244px;
  }
  .action-row { position: absolute; left: 209px; top: 286px; }
  .button-group {
    position: absolute; left: 0; top: 0;
    display: flex; height: 22px;
    border: 1px solid var(--ui-border); border-radius: 2px;
    background: #f6f7f9;
  }
  .ui-button {
    display: flex; align-items: center; gap: 3px;
    padding: 0 8px; font-size: 10px; font-weight: 700; color: var(--ui-text);
    border-right: 1px solid var(--ui-border);
  }
  .ui-button:last-child { border-right: 0; }
  .use-app {
    position: absolute; left: 398px; top: 0;
    width: 109px; height: 22px; line-height: 22px;
    text-align: center; font-size: 11.5px; color: var(--white);
    background: var(--bar-blue); border-radius: 2px;
  }
  .send-message {
    position: absolute; left: 516px; top: 0;
    width: 104px; height: 20px; line-height: 20px;
    font-size: 11.5px; color: var(--ui-text);
    background: #f6f7f9; border: 1px solid var(--ui-border); border-radius: 2px;
    display: flex; align-items: center; justify-content: center; gap: 4px;
  }
  .brand-name { font-family: "Montserrat", sans-serif; font-weight: 700; }
  .tagline { font-family: "Montserrat", sans-serif; font-weight: 700; letter-spacing: 0.6px; }
  .web-address { font-family: "Montserrat", sans-serif; font-weight: 600; }
</style>
</head>
<body>
<main class="canvas">
  <section class="page">
    <header class="top-bar">
      <span class="site-mark"></span>
      <div class="search-box">
        <div class="search-button">
          <svg width="34" height="17" viewBox="0 0 34 17"><circle cx="16" cy="7.5" r="3.6" fill="none" stroke="#4b4f56" stroke-width="1.5"/><line x1="18.6" y1="10.2" x2="21" y2="12.6" stroke="#4b4f56" stroke-width="1.6"/></svg>
        </div>
      </div>
      <span class="nav-link home">Home</span>
      <span class="nav-sep"></span>
      <span class="nav-link friends">Find Friends</span>
      <svg class="nav-icons" width="140" height="22" viewBox="0 0 140 22">
        <g fill="#1d3a6e">
          <circle cx="9" cy="7" r="3.5"/><path d="M2 18 Q9 9 16 18 Z"/>
          <circle cx="16" cy="8" r="2.8"/><path d="M13 17 Q17 11 21 17 Z"/>
        </g>
        <circle cx="37" cy="11" r="8" fill="var(--white)"/>
        <circle cx="42" cy="4" r="3.8" fill="var(--badge)"/>
        <path d="M59 16 Q59 6 65 6 Q71 6 71 16 Z" fill="var(--white)"/>
        <circle cx="65" cy="17.5" r="1.8" fill="var(--white)"/>
        <circle cx="70" cy="4" r="3.8" fill="var(--badge)"/>
        <circle cx="100" cy="11" r="8" fill="#1d3a6e"/>
        <text x="100" y="15" text-anchor="middle" font-size="11" font-weight="700" fill="var(--bar-blue)" font-family="Roboto, sans-serif">?</text>
        <path d="M124 9 L132 9 L128 13 Z" fill="#1d3a6e"/>
      </svg>
    </header>

    <aside class="side-column">
      <nav class="side-menu">
        <div class="menu-item active">Home</div>
        <div class="menu-item">About</div>
        <div class="menu-item">Photos</div>
      </nav>
    </aside>

    <svg class="profile-picture" viewBox="0 0 176 176" aria-label="Profilbild KVR">
      <rect width="176" height="176" fill="var(--paper)"/>
      <circle cx="88" cy="70" r="26" fill="none" stroke="var(--brand-blue)" stroke-width="3"/>
      <text class="brand-name" x="88" y="122" text-anchor="middle" font-size="26" fill="var(--brand-blue)">KVR</text>
      <text class="web-address" x="88" y="142" text-anchor="middle" font-size="10" fill="var(--brand-blue)">www.kvr-sport.de</text>
    </svg>

    <svg class="cover-picture" viewBox="0 0 800 304" preserveAspectRatio="none" aria-label="Titelbild KVR">
      <defs>
        <linearGradient id="photoTone" x1="0" y1="0" x2="1" y2="0">
          <stop offset="0" stop-color="var(--photo-light)"/>
          <stop offset="0.25" stop-color="#e2e2e2"/>
          <stop offset="0.5" stop-color="var(--photo-mid)"/>
          <stop offset="0.75" stop-color="#e2e2e2"/>
          <stop offset="1" stop-color="var(--photo-light)"/>
        </linearGradient>
      </defs>
      <rect class="team-photo" role="img" aria-label="Teamfoto: fünf Männer in weißen Hemden, der mittlere hält einen Fußball" width="800" height="200" fill="url(#photoTone)"/>
      <path class="blue-band" d="M0 150 Q330 215 800 148 L800 304 L0 304 Z" fill="var(--brand-blue)"/>
      <path d="M0 126 Q340 215 800 140" fill="none" stroke="var(--brand-blue)" stroke-width="1.6"/>
      <path d="M0 138 Q330 210 800 146" fill="none" stroke="var(--line-dark)" stroke-width="1.6"/>
      <path d="M0 146 Q350 212 800 150" fill="none" stroke="var(--line-dark)" stroke-width="1"/>

      <circle cx="120" cy="226" r="18" fill="none" stroke="var(--white)" stroke-width="2.4"/>
      <text class="brand-name" x="120" y="278" text-anchor="middle" font-size="24" fill="var(--white)">KVR</text>

      <text class="tagline" x="497" y="244" text-anchor="middle" font-size="20.5" fill="var(--white)">AGENTUR FÜR MANAGEMENT UND BERATUNG</text>
      <line x1="228" y1="259" x2="402" y2="259" stroke="var(--white)" stroke-width="2.5"/>
      <text class="web-address" x="497" y="266" text-anchor="middle" font-size="17" fill="var(--white)">www.kvr-sport.de</text>
      <line x1="592" y1="259" x2="766" y2="259" stroke="var(--white)" stroke-width="2.5"/>
    </svg>

    <div class="action-row">
      <div class="button-group">
        <span class="ui-button">
          <svg width="10" height="10" viewBox="0 0 10 10"><rect x="0" y="4" width="2.5" height="6" fill="#4b4f56"/><path d="M3.5 4 L6 0 Q7.5 0.5 7 3 L10 3 L9 10 L3.5 10 Z" fill="#4b4f56"/></svg>Like
        </span>
        <span class="ui-button">
          <svg width="10" height="10" viewBox="0 0 10 10"><circle cx="1.5" cy="8.5" r="1.3" fill="#4b4f56"/><path d="M0 4.5 A5.5 5.5 0 0 1 5.5 10" fill="none" stroke="#4b4f56" stroke-width="1.3"/><path d="M0 1 A9 9 0 0 1 9 10" fill="none" stroke="#4b4f56" stroke-width="1.3"/></svg>Follow
        </span>
        <span class="ui-button">
          <svg width="11" height="10" viewBox="0 0 11 10"><path d="M6 0 L11 4.5 L6 9 L6 6.3 Q2 6 0 9.5 Q1 3.5 6 2.8 Z" fill="#4b4f56"/></svg>Share
        </span>
        <span class="ui-button">···</span>
      </div>
      <div class="use-app">Use App</div>
      <div class="send-message">
        <svg width="12" height="12" viewBox="0 0 12 12"><circle cx="6" cy="6" r="5.5" fill="#4b4f56"/></svg>Send Message
      </div>
    </div>
  </section>
</main>
</body>
</html>
```